Website Redesign for Brightvale Forge

We are looking for a high-end Minimalist Design That will give potential customers the feel that they are purchasing a hand-crafted reproduction of an actual historical medieval sword. The tone or feel should like a luxury sword manufacturer.
Perhaps having a darker background with logo/text that pops more with a white glow.

Target Market(s)

Historical "efficinato" - educated history buffs interested in high end swords & armors, with a available capital for such a hobby.

Number of Pages Required

3 page

Font styles to use
Serif

Colors
1b1b1b
000000
e6e6e6
c9c9c9

Requirements
Must have
• -cart page
• -home page
• -1 product page
Nice to have
• -large images
• - Garamon or Centaur font
• - Our logo is in Trojan Pro
Should not have
• -no excessive use of colors
• -no medieval / gothic fonts

```html
<!DOCTYPE html>
<html lang="en">
<head>
<meta charset="utf-8">
<title>Brightvale Forge — Home</title>
<link href="https://fonts.googleapis.com/css2?family=Tinos:wght@400;700&family=Raleway:wght@400;500;600&display=swap" rel="stylesheet">
<style>
  :root{
    --canvas:#dcdcdc;
    --page:#ffffff;
    --ink:#1b1b1b;
    --black:#000000;
    --accent:#c9252c;
    --band:#f4f4f4;
    --footer:#262626;
    --light:#e6e6e6;
    --muted:#c9c9c9;
    --rule:#ececec;
  }
  *{margin:0;padding:0;box-sizing:border-box}
  html,body{width:1200px;height:1200px;overflow:hidden;background:var(--canvas)}
  body{position:relative;font-family:"Tinos",serif;color:var(--ink)}
  .page{position:absolute;left:72px;top:0;width:1054px;height:1124px;background:var(--page);overflow:hidden}
  .abs{position:absolute}

  .view-all{left:451px;top:18px;width:152px;height:32px;border:2px solid var(--accent);border-radius:16px;
    color:var(--accent);font-family:"Raleway",sans-serif;font-size:11px;letter-spacing:1.2px;
    display:flex;align-items:center;justify-content:center;font-weight:500}

  .hero{left:0;top:70px;width:1054px;height:376px;
    background:radial-gradient(ellipse at 78% 45%,#5a5a5a 0%,#303030 30%,#1b1b1b 65%),#1b1b1b}
  .hero .play{position:absolute;left:498px;top:111px;width:58px;height:58px;border-radius:50%;background:#fff}
  .hero .play svg{position:absolute;left:22px;top:19px}
  .hero h2{position:absolute;left:0;width:100%;top:204px;text-align:center;color:#fff;font-size:21px;line-height:27px;font-weight:700}

  .news-title{left:0;width:100%;top:472px;text-align:center;font-size:21px;font-weight:700;letter-spacing:.3px}
  .rule{top:485px;height:1px;background:var(--rule);width:268px}

  .card{top:521px;width:339px}
  .card .photo{height:221px}
  .card h3{margin-top:12px;text-align:center;font-size:16px;font-weight:700}
  .card .meta{margin-top:8px;text-align:center;font-size:7px;color:var(--ink)}
  .card .meta b{letter-spacing:.3px;margin:0 8px 0 2px}

  .mailing{left:0;top:800px;width:1054px;height:86px;background:var(--band)}
  .mailing .label{position:absolute;left:208px;top:33px;font-size:9px;font-weight:700;letter-spacing:1.8px}
  .mailing .field{position:absolute;left:370px;top:28px;width:313px;height:21px;background:#fff;border:1px solid #dedede;
    font-family:"Raleway",sans-serif;font-size:7px;color:#9a9a9a;padding:6px 4px}
  .mailing .join{position:absolute;left:724px;top:28px;width:122px;height:21px;background:var(--footer);color:#fff;
    font-size:7px;font-weight:700;display:flex;align-items:center;justify-content:center;letter-spacing:.5px}

  .footer{left:0;top:886px;width:1054px;height:238px;background:var(--footer);color:#fff}
  .brand{position:absolute;left:188px;top:42px;width:172px;text-align:center}
  .brand .mark{width:30px;height:30px;border-radius:50%;border:2px solid #fff;margin:0 auto 10px}
  .brand .name{font-size:20px;font-weight:700;line-height:22px}
  .sitemap{position:absolute;left:412px;top:42px;width:60px;text-align:center;font-size:8px;font-weight:700}
  .sitemap li{list-style:none;margin-top:10px}
  .sitemap .head{margin-bottom:0}
  .cart-icon{position:absolute;left:534px;top:70px}
  .cart-head{position:absolute;left:600px;top:42px;font-size:8px;font-weight:700}
  .cart-text{position:absolute;left:600px;top:68px;font-family:"Raleway",sans-serif;font-size:11px;line-height:15px;text-align:center;width:82px}
  .lock{position:absolute;left:708px;top:44px}
  .secure{position:absolute;left:755px;top:45px;font-family:"Raleway",sans-serif;font-size:8.5px;letter-spacing:.8px}
  .payname{position:absolute;left:762px;top:62px;font-family:"Raleway",sans-serif;font-size:24px;font-weight:600;color:#fff}
  .cards{position:absolute;left:704px;top:98px;display:flex;gap:6px}
  .cards span{width:34px;height:21px;border-radius:2px;background:var(--light)}
  .copy{position:absolute;left:0;width:100%;top:185px;text-align:center;font-family:"Raleway",sans-serif;font-size:7.5px}
  .copy u{text-decoration:underline}
</style>
</head>
<body>
<main class="page">
  <a class="abs view-all">VIEW ALL PRODUCTS</a>

  <section class="abs hero" role="img" aria-label="Black and white photo of a smith grinding a blade with sparks flying">
    <div class="play">
      <svg width="18" height="20" viewBox="0 0 18 20"><path d="M1 1 L16 10 L1 19 Z" fill="#1b1b1b"/></svg>
    </div>
    <h2>Click The Play Button To See<br>Our Swords In Action</h2>
  </section>

  <div class="abs rule" style="left:160px"></div>
  <h2 class="abs news-title">LATEST NEWS</h2>
  <div class="abs rule" style="left:626px"></div>

  <article class="abs card" style="left:2px">
    <div class="photo" role="img" aria-label="Two sword fighters sparring on grass beside a brick wall" style="background:linear-gradient(180deg,#8a6a5c 0%,#9b7b6c 55%,#5f8a3e 72%,#4f7a32 100%)"></div>
    <h3>Distance and Range</h3>
    <p class="meta">by <b>ADMIN</b> on <b>FEBRUARY 7, 2016</b></p>
  </article>
  <article class="abs card" style="left:358px">
    <div class="photo" role="img" aria-label="Large crowd of armoured reenactors with banners on a field" style="background:linear-gradient(180deg,#7a8a5e 0%,#6a5a50 40%,#7a3a34 70%,#4a4a48 100%)"></div>
    <h3>A Tale of Two Western Martial Arts</h3>
    <p class="meta">by <b>ADMIN</b> on <b>FEBRUARY 2, 2016</b></p>
  </article>
  <article class="abs card" style="left:713px">
    <div class="photo" role="img" aria-label="Instructor standing beside a wooden training post in a stone hall" style="background:linear-gradient(180deg,#6f6a60 0%,#8a8276 55%,#7a5e4c 80%,#6a4e40 100%)"></div>
    <h3>Sticks and Swords</h3>
    <p class="meta">by <b>ADMIN</b> on <b>JANUARY 27, 2016</b></p>
  </article>

  <section class="abs mailing">
    <span class="label">JOIN OUR MAILING LIST</span>
    <div class="field">Enter your email</div>
    <div class="join">JOIN</div>
  </section>

  <footer class="abs footer">
    <div class="brand">
      <div class="mark"></div>
      <div class="name">Brightvale Forge</div>
    </div>
    <ul class="sitemap">
      <li class="head" style="margin-top:0">SITEMAP</li>
      <li>My Account</li>
      <li>Blog</li>
      <li>Cart</li>
    </ul>
    <svg class="cart-icon" width="48" height="44" viewBox="0 0 48 44" fill="none" stroke="#fff" stroke-width="1.6">
      <path d="M1 3 H8 L13 30 H44"/>
      <path d="M9 9 H47 L43 24 H12"/>
      <circle cx="17" cy="38" r="4"/>
      <circle cx="38" cy="38" r="4"/>
    </svg>
    <div class="cart-head">CART</div>
    <div class="cart-text">Your cart is currently empty.</div>
    <svg class="lock" width="32" height="42" viewBox="0 0 32 42">
      <path d="M7 18 V11 a9 9 0 0 1 18 0 V18" fill="none" stroke="#bdbdbd" stroke-width="3.5"/>
      <rect x="2" y="17" width="28" height="24" rx="3" fill="#d8b544"/>
    </svg>
    <div class="secure">SECURE PAYMENTS BY</div>
    <div class="payname">SafePay</div>
    <div class="cards"><span></span><span></span><span></span><span></span></div>
    <p class="copy">© 2016 Brightvale Forge | Made By <u>Loom &amp; Line</u></p>
  </footer>
</main>
</body>
</html>
```